Marlow's Shutters RT Porter Car Wrap Design

We need our RT Porter Vans wrapped, 50%-75% of the vans covered.
We want our contact details (PH: 03)47159320, email: sales@marlowsshutters.com.au, web: www.marlowsshutters.com.au) included as well as our logo and images
Looking to incorporate our colours (green and grey) and some classy images.

Target Market(s)

All ages

Font styles to use
Serif
Sans Serif

Colors
00a990
edf8f6
474747
7f7f7f
32b8a4

Requirements
Must have
• Logo, Contact Details, colour scheme of Green and Grey, images
Should not have
• Hard to read, images to big that distracts from Logo/contact details

```html
<!DOCTYPE html>
<html lang="en">
<head>
<meta charset="utf-8">
<title>Marlow's Shutters – RT Porter Wrap</title>
<link href="https://fonts.googleapis.com/css2?family=Roboto+Condensed:wght@400;700&family=Open+Sans:wght@700&display=swap" rel="stylesheet">
<style>
  :root {
    --green: #00a990;
    --green-light: #32b8a4;
    --green-deep: #0d7f6f;
    --mint: #edf8f6;
    --grey-dark: #474747;
    --grey-mid: #7f7f7f;
    --stage: #e9e9e9;
    --white: #ffffff;
  }
  * { margin: 0; padding: 0; box-sizing: border-box; }
  html, body { width: 1200px; height: 1200px; overflow: hidden; background: var(--stage); }
  .canvas { position: relative; width: 1200px; height: 1200px; }
  .wrap-panel {
    position: absolute; left: 50px; top: 370px; width: 1100px; height: 460px;
    border-radius: 18px; overflow: hidden; background: var(--white);
    box-shadow: 0 6px 24px rgba(0,0,0,.12);
  }
  .wrap-art { position: absolute; inset: 0; }
  .brand {
    position: absolute; left: 466px; top: 112px; display: flex; align-items: center; gap: 10px;
  }
  .brand-mark { width: 16px; height: 16px; background: var(--green); flex: none; }
  .brand-name {
    font-family: "Roboto Condensed", sans-serif; font-weight: 700; font-size: 28px;
    color: var(--green); line-height: 1; white-space: nowrap;
  }
  .contact { position: absolute; left: 466px; display: flex; align-items: center; gap: 8px; color: var(--grey-dark); white-space: nowrap; }
  .contact svg { flex: none; }
  .contact-phone { top: 186px; font-family: "Roboto Condensed", sans-serif; font-weight: 700; font-size: 23px; letter-spacing: 5px; }
  .contact-email { top: 243px; font-family: "Roboto Condensed", sans-serif; font-weight: 400; font-size: 18px; }
  .contact-web { top: 299px; font-family: "Open Sans", sans-serif; font-weight: 700; font-size: 13px; }
</style>
</head>
<body>
<div class="canvas">
  <div class="wrap-panel">
    <svg class="wrap-art" width="1100" height="460" viewBox="0 0 1100 460">
      <defs>
        <linearGradient id="panelFade" x1="0" y1="0" x2="1" y2="0.3">
          <stop offset="0.35" stop-color="#ffffff"/>
          <stop offset="0.8" stop-color="#cfeee8"/>
          <stop offset="1" stop-color="#7fd3c5"/>
        </linearGradient>
        <linearGradient id="photoTone" x1="0" y1="0" x2="1" y2="1">
          <stop offset="0" stop-color="#d8d1c4"/>
          <stop offset="0.5" stop-color="#ecebe7"/>
          <stop offset="1" stop-color="#bfb8ab"/>
        </linearGradient>
        <linearGradient id="swoosh" x1="0" y1="0" x2="1" y2="0">
          <stop offset="0" stop-color="#32b8a4" stop-opacity="0.2"/>
          <stop offset="0.6" stop-color="#00a990"/>
          <stop offset="1" stop-color="#0d7f6f"/>
        </linearGradient>
      </defs>

      <rect class="panel-base" width="1100" height="460" fill="url(#panelFade)"/>

      <path class="feature-photo" role="img" aria-label="Photo of white roller shutters on a brick house"
            d="M632 0 H1100 V262 C990 250 900 250 820 240 C740 200 690 90 632 0 Z" fill="url(#photoTone)"/>
      <path class="photo-edge" d="M632 0 C690 90 740 200 820 240 C900 250 990 250 1100 262"
            fill="none" stroke="var(--green)" stroke-width="10"/>
      <path class="photo-edge-dark" d="M800 226 C900 250 1000 260 1100 300 V330 C1000 290 900 270 790 246 Z"
            fill="var(--grey-dark)"/>

      <path class="sweep-main" d="M380 340 C600 300 850 250 1100 270 V380 C850 360 600 350 380 340 Z" fill="url(#swoosh)"/>
      <path class="sweep-dark" d="M520 370 C700 330 900 320 1100 330 V350 C900 345 700 355 520 370 Z" fill="var(--grey-dark)" opacity="0.75"/>

      <rect class="band-grey" x="0" y="352" width="1100" height="38" fill="var(--grey-dark)"/>
      <path class="band-teal" d="M245 437 L300 400 C500 392 800 390 1100 390 V437 Z" fill="var(--green)"/>
      <path class="band-stripe" d="M250 430 C450 400 600 392 700 390 L260 420 Z" fill="var(--grey-dark)"/>

      <circle class="detail-ring" cx="828" cy="185" r="84" fill="var(--green-light)"/>
      <circle class="detail-photo" role="img" aria-label="Close-up photo of a roller shutter beside brickwork"
              cx="828" cy="185" r="76" fill="#cfcac0"/>
    </svg>

    <div class="brand">
      <span class="brand-mark"></span>
      <span class="brand-name">Marlow's Shutters</span>
    </div>

    <div class="contact contact-phone">
      <svg width="22" height="22" viewBox="0 0 24 24"><circle cx="12" cy="12" r="11" fill="none" stroke="#474747" stroke-width="1.5"/><path d="M8 6.5c-.8.5-1.2 1.5-.8 2.7.9 3 3.2 5.7 6.2 6.9 1.1.4 2.1 0 2.6-.8l-2-1.7-1.3.9c-1.4-.8-2.5-2-3.2-3.4l.9-1.3z" fill="#474747"/></svg>
      <span>(03)47159320</span>
    </div>
    <div class="contact contact-email">
      <svg width="26" height="26" viewBox="0 0 26 26"><circle cx="13" cy="13" r="12" fill="#32b8a4" stroke="#474747" stroke-width="1.5"/><rect x="7" y="9" width="12" height="8" fill="none" stroke="#fff" stroke-width="1.4"/><path d="M7 9l6 5 6-5" fill="none" stroke="#fff" stroke-width="1.4"/></svg>
      <span>sales@marlowsshutters.com.au</span>
    </div>
    <div class="contact contact-web">
      <svg width="26" height="26" viewBox="0 0 26 26"><circle cx="13" cy="13" r="12" fill="#32b8a4" stroke="#474747" stroke-width="1.5"/><circle cx="13" cy="13" r="6.5" fill="none" stroke="#fff" stroke-width="1.3"/><ellipse cx="13" cy="13" rx="2.8" ry="6.5" fill="none" stroke="#fff" stroke-width="1.1"/><path d="M6.5 13h13" stroke="#fff" stroke-width="1.1"/></svg>
      <span>WWW.MARLOWSSHUTTERS.COM.AU</span>
    </div>
  </div>
</div>
</body>
</html>
```